Upmarket cover for top management book, ideally unlike most common cover pages

This book is about both good management and mismanagement and introduces novel concepts such as the inverse exponential law in strategy, No doubt that these concepts will be criticized by some management scholars. However, students, a few other colleagues and key top managers find the new ideas useful and eye-opening.
The cover must help communicate a deeper vision of management as an expression of life creation and a sort of "divine" energy.

Practical details:
Print and ebook cover page plus elements of the cover for each of the three main book sections.
Title; The Harbor
Subtitle: Field methods and the quiet ripple rule
Author: Teodor M. Vasquel
Publisher: Brightwell Page Press
Width x height: 13,97 x 21,59 cm (without bleed)
Spine: 14-15 cm according to paper color

Target Market(s)

Mostly managers who did not have the opportunity of attending postgraduate management studies such as the MBA

Industry/Entity Type

Mostly high technology

Font styles to use
Serif
Sans Serif
Other font styles liked:
• Arial nova, Arial light

Requirements
Must have
• Preferably cover and back cover on white background, but any good proposals would do.
Nice to have
• An image of bright and reassuring, albeit potentially unlimited, strength. Ideally the cover design should show that good management is good for the COMMON GOOD of society
Should not have
• Please do not show images of people and no proposals reminiscent of other management and strategy book covers

```html
<!DOCTYPE html>
<html lang="en">
<head>
<meta charset="utf-8">
<title>The Harbor — Teodor M. Vasquel</title>
<link rel="stylesheet" href="https://fonts.googleapis.com/css2?family=Great+Vibes&family=Cormorant+Garamond:wght@500;600&family=Montserrat:wght@500&display=swap">
<style>
  :root {
    --page: #ffffff;
    --gold: #ecd39f;
    --gold-deep: #d9b876;
    --night: #1d1840;
    --violet: #5a2b8c;
    --indigo: #2b2f86;
    --magenta: #c43fa8;
    --ember: #f04a1e;
    --flame: #ff7a1a;
    --glow: #f7e9ff;
    --aqua: #37d6c8;
  }
  * { box-sizing: border-box; margin: 0; padding: 0; }
  html, body {
    width: 1200px;
    height: 920px;
    overflow: hidden;
    background: var(--page);
  }
  .cover {
    position: absolute;
    left: 328px;
    top: 40px;
    width: 544px;
    height: 840px;
    overflow: hidden;
    background: var(--night);
  }
  .cover-art {
    position: absolute;
    inset: 0;
    background:
      radial-gradient(ellipse 55% 40% at 88% 22%, var(--flame) 0%, var(--ember) 40%, rgba(240,74,30,0) 75%),
      radial-gradient(ellipse 45% 35% at 55% 58%, var(--glow) 0%, rgba(230,180,240,0.55) 35%, rgba(196,63,168,0) 75%),
      radial-gradient(ellipse 55% 30% at 45% 86%, var(--aqua) 0%, rgba(55,214,200,0.35) 40%, rgba(55,214,200,0) 75%),
      radial-gradient(ellipse 50% 40% at 30% 40%, var(--magenta) 0%, rgba(196,63,168,0) 70%),
      radial-gradient(ellipse 70% 60% at 10% 20%, var(--indigo) 0%, rgba(43,47,134,0) 70%),
      linear-gradient(180deg, var(--violet) 0%, var(--indigo) 55%, var(--night) 100%);
  }
  .book-title { font-size: inherit; font-weight: inherit; }
  .title-lead {
    position: absolute;
    left: 130px;
    top: 58px;
    font-family: "Great Vibes", cursive;
    font-size: 110px;
    line-height: 1;
    color: var(--gold);
  }
  .title-main {
    position: absolute;
    left: 0;
    right: 0;
    top: 172px;
    text-align: center;
    white-space: nowrap;
    font-family: "Cormorant Garamond", serif;
    font-weight: 500;
    font-size: 124px;
    line-height: 1;
    color: var(--gold);
    transform: scale(0.86, 1.3);
    transform-origin: center top;
    text-shadow: 0 2px 6px rgba(20,10,40,0.45);
  }
  .subtitle {
    position: absolute;
    right: 28px;
    top: 316px;
    text-align: right;
    white-space: nowrap;
    font-family: "Montserrat", sans-serif;
    font-weight: 500;
    font-size: 19px;
    line-height: 31px;
    color: var(--gold);
    text-transform: uppercase;
    text-shadow: 0 1px 3px rgba(20,10,40,0.4);
  }
  .author {
    position: absolute;
    left: 0;
    right: 0;
    bottom: 24px;
    text-align: center;
    white-space: nowrap;
    font-family: "Cormorant Garamond", serif;
    font-weight: 600;
    font-size: 56px;
    line-height: 1;
    color: var(--gold);
    transform: scale(0.8, 1.45);
    transform-origin: center bottom;
    text-shadow: 0 2px 6px rgba(10,5,30,0.6);
  }
</style>
</head>
<body>
  <main class="cover">
    <div class="cover-art" role="img" aria-label="Cosmic illustration: a luminous galaxy in violet, magenta and orange with a bright rainbow path of light leading into the distance"></div>
    <h1 class="book-title">
      <span class="title-lead">The</span>
      <span class="title-main">HARBOR</span>
    </h1>
    <p class="subtitle">Field methods<br>and the quiet ripple rule</p>
    <p class="author">TEODOR M. VASQUEL</p>
  </main>
</body>
</html>
```